Business card, Invoice and printable service brochure

I need a 5.5x8.5 invoice, business card and printable service template for reception desk designed for my Rug repair, restoration and cleaning business.

I have included a picture for reference

www.belkarrug.com

Columns i need in my invoice:
Type of rug, Size, Background Color, Repair needs, Notes, Price and rug cleaning disclaimer.

Target Market(s)

Higher segment clients

Industry/Entity Type

Rug Repair, Restoration and cleaning,

Requirements
Must have
• Services hast to be listed on the invoice as well as service brochure.

```html
<!DOCTYPE html>
<html lang="en">
<head>
<meta charset="utf-8">
<title>Belkar Rug – Stationery Set</title>
<link href="https://fonts.googleapis.com/css2?family=Fira+Sans:ital,wght@0,400;0,500;0,600;0,700;1,600&family=Fira+Sans+Condensed:wght@600&display=swap" rel="stylesheet">
<style>
  :root{
    --gold:#b4955e;
    --ink:#0c0c0c;
    --paper:#ffffff;
    --text:#1e1e1e;
    --bg:#c4c6c6;
    --bg-dark:#8b8b8b;
    --sans:"Fira Sans", sans-serif;
    --cond:"Fira Sans Condensed", "Fira Sans", sans-serif;
  }
  *{margin:0;padding:0;box-sizing:border-box}
  html,body{width:1135px;height:1200px;overflow:hidden;background:var(--bg)}
  body{font-family:var(--sans);color:var(--text);position:relative}
  .backdrop-shade{position:absolute;inset:0;background:var(--bg-dark);clip-path:polygon(100% 0,100% 100%,0 100%)}
  .sheet-label{position:absolute;font-size:12.5px;color:#222;font-weight:400}
  .piece{position:absolute;box-shadow:0 9px 12px -4px rgba(0,0,0,.45);overflow:hidden}
  .abs{position:absolute}
  .ico{width:7px;height:7px;fill:var(--gold);vertical-align:-1px;margin-right:4px}

  /* business card front */
  .card-front{left:70px;top:104px;width:320px;height:179px;background:var(--ink)}
  .brand-name{font-family:var(--sans);font-weight:500;color:var(--gold);letter-spacing:.04em;white-space:nowrap;line-height:1}
  .tagline{font-family:var(--sans);color:var(--gold);text-transform:uppercase;white-space:nowrap;line-height:1}
  .card-front .brand-name{left:0;right:0;top:52px;text-align:center;font-size:26px}
  .card-front .tagline{left:0;right:0;top:82px;text-align:center;font-size:5.6px;letter-spacing:.38em}
  .stripe{position:absolute;left:0;right:0}
  .gold{background:var(--gold)}
  .black{background:var(--ink)}

  /* business card back */
  .card-back{left:591px;top:104px;width:320px;height:179px;background:var(--paper)}
  .person{left:33px;top:21px;font-size:10px;letter-spacing:.02em}
  .person b{font-weight:700}
  .person small{display:block;font-size:7.6px;margin-top:1px}
  .card-contacts{left:33px;top:103px;font-size:7px;line-height:18.8px;list-style:none}
  .card-divider{left:187px;top:89px;width:1px;height:90px;background:var(--gold)}
  .card-back .brand-name{left:196px;top:106px;font-size:15.5px;color:var(--ink)}
  .card-back .tagline{left:196px;top:122px;font-size:3.6px;letter-spacing:.3em;color:var(--ink)}
  .card-hours{left:196px;top:137px;font-size:7.2px;line-height:10.3px}

  /* documents */
  .doc{top:362px;width:496px;height:766px;background:var(--paper)}
  .doc-front{left:70px}
  .doc-back{left:591px}
  .doc-header{left:0;top:0;width:496px;height:123px;background:var(--ink)}
  .doc-header .brand-name{left:27px;top:21px;font-size:40px;letter-spacing:.02em}
  .doc-header .tagline{left:26px;top:57px;font-size:9px;letter-spacing:.42em}
  .doc-contact{font-size:8.6px;color:#fff;white-space:nowrap}
  .doc-divider{left:328px;top:21px;width:1.5px;height:86px;background:var(--gold)}
  .doc-hours{left:359px;top:67px;font-size:8.4px;line-height:13.3px;color:#fff}
  .doc-hours b{font-weight:700}

  /* invoice */
  .field-label{font-size:8.6px}
  .table-head{left:0;top:167px;width:496px;height:30px;background:var(--gold)}
  .col-title{top:0;height:30px;line-height:30px;text-align:center;font-size:10px;font-weight:600;color:#2a2a2a}
  .col-rule{width:1px;background:var(--gold)}
  .row-rule{left:16px;width:463px;height:1px;background:var(--gold)}
  .totals{font-size:9.5px;line-height:12px}
  .totals b{font-weight:600}
  .total-box{left:334px;top:565px;width:142px;height:31px;background:var(--gold);font-size:10px;font-weight:600;padding:9px 0 0 9px;color:#2a2a2a}
  .repair-needs{left:27px;top:602px;width:300px;font-size:9.5px;font-weight:600;display:flex;align-items:center;gap:5px}
  .repair-needs::after,.disclaimer-title::after{content:"";flex:1;height:1px;background:#333}
  .note{left:27px;top:617px;width:440px;font-size:8.6px;line-height:13px}
  .note b{font-weight:700}
  .disclaimer-title{left:27px;top:665px;width:291px;font-size:6px;font-weight:600;font-style:italic;display:flex;align-items:center;gap:4px}
  .disclaimer{left:27px;top:676px;width:299px;font-size:5.9px;line-height:8.9px;text-align:justify}
  .bill-divider{left:334px;top:657px;width:1.5px;height:90px;background:var(--gold)}
  .bill-title{left:345px;top:654px;font-size:15px;font-weight:600;color:var(--gold)}
  .bill-lines{left:345px;top:676px;font-size:8px;line-height:17.7px;list-style:none}

  /* services */
  .services-pill{left:205px;top:147px;width:87px;height:21px;border:1.5px solid var(--gold);background:var(--ink);border-radius:11px;color:var(--gold);font-family:var(--cond);font-weight:600;font-size:13px;text-align:center;line-height:18px}
  .service{left:97px;width:366px}
  .service h3{font-family:var(--cond);font-weight:600;font-size:9.6px;color:var(--gold);line-height:11px;margin-bottom:1px}
  .service p{font-size:7.5px;line-height:9.7px;text-align:justify;margin-bottom:4.6px}
  .service-icon{width:39px;height:39px;border-radius:50%;background:var(--gold);box-shadow:0 2px 0 #2a2a2a;left:25px}
</style>
</head>
<body>
<svg width="0" height="0" style="position:absolute" aria-hidden="true">
  <symbol id="i-pin" viewBox="0 0 10 10"><path d="M5 0a3.5 3.5 0 0 0-3.5 3.5C1.5 6 5 10 5 10s3.5-4 3.5-6.5A3.5 3.5 0 0 0 5 0zm0 4.8a1.3 1.3 0 1 1 0-2.6 1.3 1.3 0 0 1 0 2.6z"/></symbol>
  <symbol id="i-phone" viewBox="0 0 10 10"><path d="M2 .5l1.8 2.2-1 1.2a6 6 0 0 0 3.3 3.3l1.2-1L9.5 8 8.3 9.5C4 9.5.5 6 .5 1.7z"/></symbol>
  <symbol id="i-mail" viewBox="0 0 10 10"><path d="M.5 2h9v6h-9zm1 .8L5 5.4l3.5-2.6"/></symbol>
  <symbol id="i-web" viewBox="0 0 10 10"><path d="M5 .5a4.5 4.5 0 1 0 0 9 4.5 4.5 0 0 0 0-9zm0 1c.7.7 1.1 1.9 1.2 3H3.8c.1-1.1.5-2.3 1.2-3zM1.6 5.5h1.2c.1 1.1.4 2 .8 2.6A3.5 3.5 0 0 1 1.6 5.5zm4.8 2.6c.4-.6.7-1.5.8-2.6h1.2a3.5 3.5 0 0 1-2 2.6zM3.8 5.5h2.4c-.1 1-.5 2-1.2 2.6-.7-.6-1.1-1.6-1.2-2.6z"/></symbol>
</svg>

<div class="backdrop-shade"></div>

<div class="sheet-label" style="left:69px;top:82px">business card front</div>
<div class="sheet-label" style="left:590px;top:82px">business card back</div>
<div class="sheet-label" style="left:69px;top:338px">Invoice front</div>
<div class="sheet-label" style="left:590px;top:338px">Invoice back</div>

<!-- Business card front -->
<section class="piece card-front">
  <div class="abs brand-name">BELKAR RUG</div>
  <div class="abs tagline">Repair | Restoration | Cleaning</div>
  <div class="stripe gold" style="top:133px;height:5px"></div>
  <div class="stripe gold" style="top:143px;height:5px"></div>
</section>

<!-- Business card back -->
<section class="piece card-back">
  <div class="abs person"><b>DANIEL</b> REYES<small>Director</small></div>
  <div class="stripe gold" style="top:64px;height:6px"></div>
  <div class="stripe black" style="top:70px;height:6px"></div>
  <div class="stripe gold" style="top:76px;height:4px"></div>
  <ul class="abs card-contacts">
    <li><svg class="ico"><use href="#i-pin"/></svg>1420 Marlow Ave, Evanston, IL 60201</li>
    <li><svg class="ico"><use href="#i-phone"/></svg>(847)555-0192</li>
    <li><svg class="ico"><use href="#i-mail"/></svg>info@belkarrug.com</li>
    <li><svg class="ico"><use href="#i-web"/></svg>www.belkarrug.com</li>
  </ul>
  <div class="abs card-divider"></div>
  <div class="abs brand-name">BELKAR RUG</div>
  <div class="abs tagline">Repair | Restoration | Cleaning</div>
  <div class="abs card-hours">Monday - Friday 9AM–5PM<br>Saturday 12PM–5PM<br>Sunday Closed</div>
</section>

<!-- Invoice front -->
<section class="piece doc doc-front">
  <header class="abs doc-header">
    <div class="abs brand-name">BELKAR RUG</div>
    <div class="abs tagline">Repair | Restoration | Cleaning</div>
    <div class="abs doc-contact" style="left:26px;top:80px"><svg class="ico"><use href="#i-pin"/></svg>1420 Marlow Ave, Evanston, IL 60201</div>
    <div class="abs doc-contact" style="left:26px;top:93px"><svg class="ico"><use href="#i-phone"/></svg>(847)555-0192</div>
    <div class="abs doc-contact" style="left:193px;top:80px"><svg class="ico"><use href="#i-mail"/></svg>info@belkarrug.com</div>
    <div class="abs doc-contact" style="left:193px;top:93px"><svg class="ico"><use href="#i-web"/></svg>www.belkarrug.com</div>
    <div class="abs doc-divider"></div>
    <div class="abs doc-hours">Monday - Friday 9AM–5PM<br>Saturday 12PM–5PM<br><b>SUNDAY CLOSED</b></div>
  </header>
  <div class="stripe gold" style="top:123px;height:4px"></div>
  <div class="stripe black" style="top:127px;height:3px"></div>
  <div class="stripe gold" style="top:130px;height:4px"></div>

  <div class="abs field-label" style="left:37px;top:146px">Date:</div>
  <div class="abs field-label" style="left:358px;top:147px">Invoice NO.</div>

  <div class="abs table-head">
    <div class="abs col-title" style="left:16px;width:128px">Type of Rug</div>
    <div class="abs col-title" style="left:144px;width:111px">Background Color</div>
    <div class="abs col-title" style="left:255px;width:64px">SIZE</div>
    <div class="abs col-title" style="left:319px;width:70px">PRICE</div>
    <div class="abs col-title" style="left:389px;width:98px">TOTAL</div>
    <div class="abs col-rule" style="left:144px;top:3px;height:24px;background:#fff"></div>
    <div class="abs col-rule" style="left:255px;top:3px;height:24px;background:#fff"></div>
    <div class="abs col-rule" style="left:319px;top:3px;height:24px;background:#fff"></div>
    <div class="abs col-rule" style="left:389px;top:3px;height:24px;background:#fff"></div>
  </div>
  <div class="abs col-rule" style="left:144px;top:203px;height:323px"></div>
  <div class="abs col-rule" style="left:255px;top:203px;height:323px"></div>
  <div class="abs col-rule" style="left:319px;top:203px;height:323px"></div>
  <div class="abs col-rule" style="left:389px;top:203px;height:323px"></div>
  <div class="abs row-rule" style="top:243px"></div>
  <div class="abs row-rule" style="top:291px"></div>
  <div class="abs row-rule" style="top:339px"></div>
  <div class="abs row-rule" style="top:388px"></div>
  <div class="abs row-rule" style="top:436px"></div>
  <div class="abs row-rule" style="top:484px"></div>

  <div class="abs totals" style="left:27px;top:537px"><b>Payment Info:</b><br>Account:<br>Bank Detail:</div>
  <div class="abs totals" style="left:345px;top:537px"><b>Sub Total:</b><br><b>Tax</b></div>
  <div class="abs total-box">Total</div>

  <div class="abs repair-needs">Repair Needs</div>
  <p class="abs note"><b>NOTE</b> that in some instances, cleaning/treatment of carpets (due to the sudden rise in humidity) can trigger the alarm on Carbon Monoxide Detectors. There is no need for concern</p>

  <div class="abs disclaimer-title">RUG CLEANING DISCLAIMER.</div>
  <p class="abs disclaimer">According to our current policy with Belkar Rug we are not covered for work be carried out on carpets and upholstery only that which could be damaged near to it. However if we require all treatment cover we have to have a disclaimer notice in place. I want to make sure I,m covering every aspect. Areas like warning clients that the carpets will remian damp for a period of time and taking care when transfering from a damp area to say a tiled floor or vinyl covering where they can slip over. Recently heard of a case where cleaner had no disclaimer, cleaned carpets, owner came home, had a look at his work, went back into her hall which was mosaic tiles, slipped over because her shoes were wet and broke her wrists. He was sued for not warning her that this could happen.</p>

  <div class="abs bill-divider"></div>
  <div class="abs bill-title">Invoice to</div>
  <ul class="abs bill-lines">
    <li>Client Name</li>
    <li>Street Address Lane</li>
    <li>Client City</li>
    <li>Mobile</li>
  </ul>
</section>

<!-- Invoice back: services -->
<section class="piece doc doc-back">
  <header class="abs doc-header">
    <div class="abs brand-name">BELKAR RUG</div>
    <div class="abs tagline">Repair | Restoration | Cleaning</div>
    <div class="abs doc-contact" style="left:26px;top:80px"><svg class="ico"><use href="#i-pin"/></svg>1420 Marlow Ave, Evanston, IL 60201</div>
    <div class="abs doc-contact" style="left:26px;top:93px"><svg class="ico"><use href="#i-phone"/></svg>(847)555-0192</div>
    <div class="abs doc-contact" style="left:193px;top:80px"><svg class="ico"><use href="#i-mail"/></svg>info@belkarrug.com</div>
    <div class="abs doc-contact" style="left:193px;top:93px"><svg class="ico"><use href="#i-web"/></svg>www.belkarrug.com</div>
    <div class="abs doc-divider"></div>
    <div class="abs doc-hours">Monday - Friday 9AM–5PM<br>Saturday 12PM–5PM<br><b>SUNDAY CLOSED</b></div>
  </header>
  <div class="stripe gold" style="top:123px;height:4px"></div>
  <div class="stripe black" style="top:127px;height:3px"></div>
  <div class="stripe gold" style="top:130px;height:4px"></div>

  <div class="abs services-pill">SERVICES</div>

  <div class="abs service-icon" style="top:201px" role="img" aria-label="Stain removal icon"></div>
  <div class="abs service-icon" style="top:281px" role="img" aria-label="Shearing scissors icon"></div>
  <div class="abs service-icon" style="top:350px" role="img" aria-label="Rug cleaning icon"></div>
  <div class="abs service-icon" style="top:433px" role="img" aria-label="Rug alteration icon"></div>
  <div class="abs service-icon" style="top:492px" role="img" aria-label="Rug blocking and stretching icon"></div>
  <div class="abs service-icon" style="top:600px" role="img" aria-label="Rug repair icon"></div>
  <div class="abs service-icon" style="top:696px" role="img" aria-label="Moth removal icon"></div>

  <article class="abs service" style="top:183px">
    <h3>STAIN REMOVAL</h3>
    <p>Having kids or pets in your home means you will occasionally experience stains on your rug. While some you can easily remove using water and detergent, other stubborn stains may require the attention of a professional rug cleaner.</p>
    <p>Professional rug cleaners understand the difference between a spot and a stain on your rug. Thus, they will clean deeper into the fabric eliminating all traces of the spill.</p>
  </article>
  <article class="abs service" style="top:263px">
    <h3>SHEARING</h3>
    <p>After cleaning your rug, you may notice that it may begin to shear and lose its shape over time. Shearing may result from too much exposure to the sun, making the rug lose some of its fibers.</p>
    <p>By engaging restoration services, they will shear your rug through light shaving to give it a vibrant new look. Shearing also helps your rug have an even look if one part of the rug has worn out.</p>
  </article>
  <article class="abs service" style="top:334px">
    <h3>RUG CLEANING</h3>
    <p>Do you want to keep your rug free from dust and allergens? Then, it is essential to consider a professional rug cleaning service. Rug cleaning involves a ten-step process: inspection, planning, dust removal, rinsing in a rug bath, scrubbing, water extraction, centrifuge drying, hanging, final inspection, and wrapping.</p>
    <p>These stages ensure a through clean of your rug from the surface to the fibers, prolonging its lifespan and removing all stubborn stains and allergens.</p>
  </article>
  <article class="abs service" style="top:424px">
    <h3>RUG ALTERATION</h3>
    <p>Have you move houses or desire to have your rug fit in a new room? Professional rug restoration, repair, and cleaning service can carefully alter your rug’s size and shape to ensure a perfect fit in the desired room.</p>
  </article>
  <article class="abs service" style="top:478px">
    <h3>RUG BLOCKING AND STRETCHING</h3>
    <p>If you have heavy traffic coming into your home, you may experience wrinkles and waves on your rug, posing a safety risk for you and your family. Besides, wrinkles on your rug may spoil its appearance and beauty, affecting its aesthetic appeal.</p>
    <p>But, a professional rug restoration service will block and stretch your rug to restore its original shape and appearance.</p>
    <p>The process involves brushing the rug, rolling it, and unrolling it to achieve a straight shape. In addition, it also prevents your rug’s corners from curling up.</p>
  </article>
  <article class="abs service" style="top:584px">
    <h3>TEAR AND WEAR OR MAJOR RUG REPAIR</h3>
    <p>Foot traffic, the weight of furniture, and pets can contribute to the wear and tear of your rug. So despite your rug being of original quality, it can still get damaged.</p>
    <p>With common types of restoration services such as internal damage, end loss, edge damage, and foundation wear, a professional rug restoration service will restore your rug to its original state.</p>
    <p>Whether it’s a major or minor repair or your rug is traditional, modern, or antique, rug restoration service will have your rug looking new.</p>
  </article>
  <article class="abs service" style="top:679px">
    <h3>MOTH REMOVAL</h3>
    <p>Warm weather and hot temperatures in your house create a habitable area for months to thrive. However, the presence of months in your home can cause damage to your rug since they feed on the natural fiber and woolen areas of your rug.</p>
    <p>Getting professional cleaning services will help you remove traces of months and moth larvae, promoting the longevity of your rug.</p>
  </article>
</section>
</body>
</html>
```